Gourmet Restaurant take out menu

We need a take out menu design that is trendy for a casual upscale Italian restaurant with a vast menu. This menu must be able to be 4 color and reproducible in large quantities to be bulked mailed or inserted into a daily paper. It must also maintain a theme that can be crossed over to our in house dining menu and specials menu.
OUR WEBSITE:
www.bellavistoplates.example
For the content, go to the Menu section of our website. We are interested in the design scheme and a template to use.
Target Market(s)
families, sinle individuals seeking take out meals and delivery
Industry/Entity Type
Restaurant
Look and feel
Each slider illustrates characteristics of the customer's brand and the style your logo design should communicate.

```html
<!DOCTYPE html>
<html lang="en">
<head>
<meta charset="utf-8">
<title>Bella Visto Plates – Take Out Menu</title>
<link href="https://fonts.googleapis.com/css2?family=Alegreya:wght@700;800&family=Crimson+Text:wght@400;600&display=swap" rel="stylesheet">
<style>
:root{
  --stage:#e4e4e4;
  --red:#9c1f1f;
  --red-dark:#7d1414;
  --accent:#a83a2a;
  --tan:#d8c7a5;
  --tan-light:#e3d5b8;
  --cream:#f4efe4;
  --ink:#24170f;
  --muted:#4a3a2e;
}
*{margin:0;padding:0;box-sizing:border-box}
html,body{width:1200px;height:787px;overflow:hidden;background:var(--stage)}
.canvas{position:relative;width:1200px;height:787px;font-family:"Crimson Text",Georgia,serif;color:var(--ink)}
.page{position:absolute;background:var(--tan)}
.page-left{left:19px;top:22px;width:565px;height:736px;border:4px solid var(--red)}
.page-right{left:602px;top:22px;width:572px;height:736px;background:var(--red)}
.page-right .inner{position:absolute;left:6px;top:6px;right:6px;bottom:0;background:var(--tan);border-radius:10px 10px 0 0}
.photo{position:absolute}
.photo-pizza{left:19px;top:22px;width:290px;height:110px;background:linear-gradient(120deg,#8a3b18,#c9742e 45%,#e2b35a 70%,#9b4a1c)}
.photo-burger{left:300px;top:22px;width:284px;height:110px;background:linear-gradient(180deg,#c9813c,#e6b35c 30%,#3a2414 50%,#d63a22 62%,#e5c040 72%,#b06b2e)}
.tan-body{position:absolute;left:23px;top:120px;width:557px;height:634px;background:var(--tan);border-radius:14px 14px 0 0}
.arch{position:absolute;left:192px;top:52px;width:222px;height:110px;background:var(--tan);border-radius:111px 111px 0 0;border-top:1.5px solid var(--accent)}
.brand{position:absolute;left:192px;top:74px;width:222px;text-align:center;color:var(--red)}
.brand-name,.brand-sub{font-family:"Alegreya",Georgia,serif;font-weight:800;font-size:31px;line-height:1}
.box{position:absolute;background:var(--cream);padding:6px 9px}
.heading{position:absolute;font-family:"Alegreya",Georgia,serif;font-weight:800;text-align:center;color:var(--ink);font-size:19px;line-height:1}
.heading.small{font-size:12px}
.tag{position:absolute;border:1px solid var(--accent);border-top:none;color:var(--accent);font-size:4.6px;text-transform:uppercase;text-align:center;line-height:1.6;padding:3px 6px;letter-spacing:.1px}
.tag.single{white-space:nowrap;letter-spacing:0;font-size:4.4px;padding:3px 4px}
.note{position:absolute;text-align:center;color:var(--accent);font-size:4.8px;line-height:1.55;text-transform:uppercase}
.note .plain{text-transform:none}
.item{margin-bottom:1.2px}
.row{display:flex;justify-content:space-between;align-items:baseline;font-size:7.6px;font-weight:600;line-height:1.15}
.row .price{font-weight:400;font-size:6.6px}
.desc{font-size:4.4px;line-height:1.35;color:var(--muted);width:82%}
.cols{display:flex;gap:14px}
.cols>div{flex:1}
.cols .row{font-weight:400;font-size:7px;line-height:1.24}
.list .row{font-weight:400}
.photo-strip{position:absolute;top:668px;height:90px}
.ph-steak{left:608px;width:192px;background:linear-gradient(135deg,#5f7f3a,#8a3a22 55%,#3b1b12)}
.ph-pasta{left:802px;width:176px;background:linear-gradient(135deg,#2a1a12,#c24a24 45%,#e28a3a 75%,#4a2a1a)}
.ph-gnocchi{left:980px;width:188px;background:linear-gradient(135deg,#3f6b28,#d9c38c 55%,#f1e6c2)}
</style>
</head>
<body>
<div class="canvas">

  <section class="page page-left" aria-label="Menu front"></section>
  <div class="photo photo-pizza" role="img" aria-label="Photo of a pizza with olives, peppers and cheese"></div>
  <div class="photo photo-burger" role="img" aria-label="Photo of a cheeseburger with tomato and lettuce"></div>
  <div class="tan-body"></div>
  <div class="arch"></div>
  <div class="brand">
    <div class="brand-name">Bella Visto</div>
    <div class="brand-sub">Plates</div>
  </div>

  <h2 class="heading" style="left:30px;top:150px;width:270px">Gourmet Pizza</h2>
  <p class="note" style="left:30px;top:174px;width:270px">
    <span class="plain">Toppings for 1.99</span><br>
    Ham · Broccoli · Extra Cheese · Tomatoes Hot or Sweet Peppers · Roasted Peppers · Pepperoni · Spinach ·<br>
    Italian Sausage · Black Olives · Green Peppers · Mushrooms · Onions · Anchovies · Grilled Chicken ·<br>
    Meatball Bacon and Ricotta 3.00<br>
    <span class="plain">10" Individual, 12" Medium, 16" Large<br>Pizza By The Slice - Plain 1.99, Veggie 2.99</span>
  </p>

  <div class="box" style="left:30px;top:232px;width:270px;height:224px">
    <div class="item"><div class="row"><span>Plain Cheese</span><span class="price">8.99/11.99/12.99</span></div></div>
    <div class="item"><div class="row"><span>Traditional White</span><span class="price">8.99/11.59/13.99</span></div><div class="desc">Olive oil, garlic, mozzarella cheese.</div></div>
    <div class="item"><div class="row"><span>Chicken Bacon Ranch</span><span class="price">10.99/14.99/16.99</span></div><div class="desc">Garlic chicken, bacon, pepperjack and cheddar cheese, red onions, diced tomatoes, drizzle of ranch dressing.</div></div>
    <div class="item"><div class="row"><span>Bronx Bomber</span><span class="price">11.99/14.99/16.99</span></div><div class="desc">Sausage, prosciutto ham, oregano, crumbled bleu and mozzarella cheese.</div></div>
    <div class="item"><div class="row"><span>Buffalo Chicken</span><span class="price">10.99/14.99/16.99</span></div><div class="desc">Buffalo sauce, chicken, mozzarella cheese, side of bleu cheese dressing.</div></div>
    <div class="item"><div class="row"><span>Gourmet Special</span><span class="price">12.99/16.99/18.99</span></div><div class="desc">Pepperoni, sausage, bell peppers, mushrooms, onion, mozzarella cheese.</div></div>
    <div class="item"><div class="row"><span>Margarita</span><span class="price">8.99/11.99/13.99</span></div><div class="desc">Fresh basil, tomato, buffalo mozzarella cheese.</div></div>
    <div class="item"><div class="row"><span>Roasted Vegetable</span><span class="price">11.99/14.99/16.99</span></div><div class="desc">Eggplant, red and yellow peppers, onions, artichokes, Kalamata olives, tomatoes, mozzarella cheese. Veggie lover olive oil, garlic, broccoli, spinach, tomato, mozzarella cheese.</div></div>
    <div class="item"><div class="row"><span>Sweet Hawaiian</span><span class="price">11.99/14.99/16.99</span></div><div class="desc">Pineapple, tomatoes, ham, mozzarella cheese.</div></div>
    <div class="item"><div class="row"><span>Spinach and Artichoke</span><span class="price">8.99/11.99/12.99</span></div><div class="desc">Spinach, artichoke hearts, basil, mozzarella, parmesan cheese.</div></div>
    <div class="item"><div class="row"><span>Philly Cheese Steak</span><span class="price">11.99/14.99/16.99</span></div><div class="desc">Philly steak, green peppers, onions, provolone, American cheese.</div></div>
    <div class="item"><div class="row"><span>Grandma's Pie</span><span class="price">14.99</span></div><div class="desc">Thin crust pizza topped with mozzarella, tomato sauce, buffalo mozzarella, fresh basil, olive oil. (One Size)</div></div>
  </div>

  <h3 class="heading small" style="left:30px;top:463px;width:270px">Hot Subs - Add Cheese for $0.59</h3>
  <div class="box" style="left:30px;top:478px;width:270px;height:102px">
    <div class="cols">
      <div>
        <div class="row"><span>Cheesesteak</span><span class="price">6.59</span></div>
        <div class="row"><span>Bacon Cheesesteak</span><span class="price">7.59</span></div>
        <div class="row"><span>Steak Sub</span><span class="price">6.29</span></div>
        <div class="row"><span>Chicken Parmigiana</span><span class="price">6.99</span></div>
        <div class="row"><span>Pepper, Egg, &amp; Cheese</span><span class="price">6.29</span></div>
        <div class="row"><span>Pizza Cheesesteak</span><span class="price">6.99</span></div>
        <div class="row"><span>Meatball Parmigiana</span><span class="price">6.99</span></div>
        <div class="row"><span>Mushroom Cheesesteak</span><span class="price">6.99</span></div>
        <div class="row"><span>Veal Parmigiana</span><span class="price">7.99</span></div>
      </div>
      <div>
        <div class="row"><span>Pepper Cheesesteak</span><span class="price">6.99</span></div>
        <div class="row"><span>Vegetarian with Cheese</span><span class="price">6.59</span></div>
        <div class="row"><span>Eggplant Parmigiana</span><span class="price">6.59</span></div>
        <div class="row"><span>Chicken Cheesesteak</span><span class="price">6.99</span></div>
        <div class="row"><span>Sausage Parmigiana</span><span class="price">7.59</span></div>
        <div class="row"><span>Grilled Chicken</span><span class="price">6.59</span></div>
        <div class="row"><span>Cheeseburger Sub</span><span class="price">7.59</span></div>
        <div class="row"><span>Chicken Cacciatore</span><span class="price">7.59</span></div>
        <div class="row"><span>Steak Cacciatore</span><span class="price">7.59</span></div>
        <div class="row"><span>Sausage, Peppers, &amp; Onion</span><span class="price">6.99</span></div>
      </div>
    </div>
  </div>

  <h3 class="heading small" style="left:30px;top:584px;width:270px">Cold Subs - Add Cheese for $0.59</h3>
  <div class="box" style="left:30px;top:600px;width:270px;height:44px">
    <div class="cols">
      <div>
        <div class="row"><span>Regular Italian</span><span class="price">6.59</span></div>
        <div class="row"><span>Tuna</span><span class="price">6.59</span></div>
        <div class="row"><span>Roast Beef</span><span class="price">7.59</span></div>
        <div class="row"><span>Imported Ham</span><span class="price">6.59</span></div>
      </div>
      <div>
        <div class="row"><span>Roast Turkey</span><span class="price">6.99</span></div>
        <div class="row"><span>Provolone</span><span class="price">6.59</span></div>
        <div class="row"><span>Capicola, Salami, &amp; Provolone</span><span class="price">6.99</span></div>
        <div class="row"><span>Chicken Salad</span><span class="price">6.99</span></div>
      </div>
    </div>
  </div>

  <h2 class="heading" style="left:30px;top:661px;width:270px">Sandwichs</h2>
  <div class="tag single" style="left:36px;top:682px;width:258px">8oz certified black angus beef, served on a kaiser roll with french fries and a fried pickle</div>
  <div class="box" style="left:30px;top:704px;width:270px;height:52px">
    <div class="item"><div class="row"><span>Bruschetta Chicken</span><span class="price">7.59</span></div><div class="desc">Bruschetta salsa, pesto, provolone cheese, balsamic drizzle on a French baguette, served with French fries.</div></div>
    <div class="item"><div class="row"><span>Chicken Parmigiana</span><span class="price">7.59</span></div><div class="desc">Served on a Kaiser roll with French fries.</div></div>
  </div>

  <div class="box" style="left:308px;top:142px;width:264px;height:230px">
    <div class="item"><div class="row"><span>Chicken Portabella</span><span class="price">8.59</span></div><div class="desc">Grilled chicken, roasted red peppers, grilled portabella, lettuce, provolone and a creamy peppercorn aioli, on a French baguette, served with French fries</div></div>
    <div class="item"><div class="row"><span>Classic BLT</span><span class="price">6.59</span></div><div class="desc">Served with potato chips.</div></div>
    <div class="item"><div class="row"><span>Crab Cake</span><span class="price">9.99</span></div><div class="desc">Lettuce, tomato and tartar sauce, served on a Kaiser roll with French fries.</div></div>
    <div class="item"><div class="row"><span>Fish Taco</span><span class="price">7.99</span></div><div class="desc">Fried wahoo in a flour tortilla with chipotle mayo, shredded lettuce, red onion and pico de gallo, finished with an avocado cream, served with potato chips.</div></div>
    <div class="item"><div class="row"><span>French Dip</span><span class="price">8.59</span></div><div class="desc">Thinly sliced Roast beef on a French baguette served with au jus, creamy horseradish sauce and French fries.</div></div>
    <div class="item"><div class="row"><span>Grilled Cheese</span><span class="price">2.99</span></div><div class="desc">Served with potato chips.</div></div>
    <div class="item"><div class="row"><span>Grilled Chicken</span><span class="price">4.99 / 6.99</span></div><div class="desc">Add bacon, ham or tomato. Lettuce, tomato, served on a Kaiser roll with French fries.</div></div>
    <div class="item"><div class="row"><span>Grilled Chicken Club</span><span class="price">8.99</span></div><div class="desc">Bacon, avocado, Swiss cheese, lettuce, tomato and roasted garlic mayonnaise on a French baguette.</div></div>
    <div class="item"><div class="row"><span>Italian Eggplant</span><span class="price">7.99</span></div><div class="desc">Grilled eggplant, roasted red peppers, red onion, melted mozzarella and garlic aioli on a French baguette.</div></div>
    <div class="item"><div class="row"><span>Roasted Turkey Cobb</span><span class="price">8.99</span></div><div class="desc">Roasted turkey breast, lettuce, tomatoes, avocado, bacon, bleu cheese dressing and Dijon mayonnaise, served on a French baguette.</div></div>
    <div class="item"><div class="row"><span>Tuna Melt</span><span class="price">6.99</span></div><div class="desc">Served with French fries.</div></div>
    <div class="item"><div class="row"><span>Turkey Club</span><span class="price">7.59</span></div><div class="desc">Served with potato chips.</div></div>
  </div>

  <h2 class="heading" style="left:308px;top:387px;width:264px">Awesome Burgers</h2>
  <div class="tag" style="left:350px;top:412px;width:180px">8oz certified black angus beef, served on a kaiser roll with french fries and a fried pickle</div>
  <div class="box" style="left:308px;top:436px;width:264px;height:142px">
    <div class="item"><div class="row"><span>Cheeseburger</span><span class="price">7.99</span></div></div>
    <div class="item"><div class="row"><span>Bacon Cheddar</span><span class="price">8.99</span></div><div class="desc">Applewood smoked bacon, sharp cheddar.</div></div>
    <div class="item"><div class="row"><span>Blue Cheese BLT</span><span class="price">9.59</span></div><div class="desc">Bacon, lettuce, tomato, onion, mayonnaise, bleu cheese.</div></div>
    <div class="item"><div class="row"><span>California</span><span class="price">9.99</span></div><div class="desc">Avocado, roasted green chilies, pepper jack cheese, chipotle mayo, ranch dressing.</div></div>
    <div class="item"><div class="row"><span>Gourmet Sliders</span><span class="price">8.99</span></div><div class="desc">3 bite-sized burgers with American cheese on mini potato rolls.</div></div>
    <div class="item"><div class="row"><span>Mushroom Swiss</span><span class="price">9.99</span></div><div class="desc">Sautéed mushrooms, onions and mayo topped with Swiss cheese.</div></div>
    <div class="item"><div class="row"><span>Portabella</span><span class="price">8.59</span></div><div class="desc">Angus burger, roasted portabella, melted provolone cheese.</div></div>
    <div class="item"><div class="row"><span>Pub</span><span class="price">9.99</span></div><div class="desc">House steak sauce and mayo, topped with onion rings, bleu cheese.</div></div>
    <div class="item"><div class="row"><span>Smokehouse Barbecue</span><span class="price">9.99</span></div><div class="desc">Smoked bacon, melted cheddar cheese, crispy onion strings, tangy barbecue-ranch sauce.</div></div>
  </div>

  <h2 class="heading" style="left:308px;top:594px;width:264px">Gorbolis &amp; Gorzones</h2>
  <div class="tag single" style="left:313px;top:614px;width:254px">Available in spinach, sundried tomato and flour tortilla, served with french fries &amp; a fried pickle</div>
  <div class="box" style="left:308px;top:630px;width:264px;height:126px">
    <div class="item"><div class="row"><span>Buffalo Chicken</span><span class="price">7.99</span></div><div class="desc">Buffalo sauce, shredded lettuce, bleu cheese dressing.</div></div>
    <div class="item"><div class="row"><span>Caprese Wrap</span><span class="price">8.99</span></div><div class="desc">Chicken, buffalo mozzarella, tomato, Romaine lettuce drizzled with a balsamic reduction.</div></div>
    <div class="item"><div class="row"><span>Chicken Caesar</span><span class="price">7.99</span></div><div class="desc">Romaine lettuce, classic Caesar salad dressing.</div></div>
    <div class="item"><div class="row"><span>Italian Chicken</span><span class="price">7.99</span></div><div class="desc">Breaded chicken tenders, cheddar cheese, lettuce, tomato, ranch dressing.</div></div>
    <div class="item"><div class="row"><span>Roman</span><span class="price">7.99</span></div><div class="desc">Chicken, roasted peppers, shredded lettuce, basil mayonnaise, mozzarella cheese.</div></div>
    <div class="item"><div class="row"><span>Santa Fe</span><span class="price">8.59</span></div><div class="desc">Chicken, guacamole, tomato, cheddar cheese, lettuce, tortilla strips, served with a side of salsa.</div></div>
    <div class="item"><div class="row"><span>The Philly</span><span class="price">7.99</span></div><div class="desc">Philly steak, provolone, sautéed onions, peppers.</div></div>
  </div>

  <section class="page page-right" aria-label="Menu back"><div class="inner"></div></section>

  <h2 class="heading" style="left:610px;top:38px;width:270px">Sandwichs</h2>
  <div class="tag single" style="left:622px;top:60px;width:246px">8oz certified black angus beef, served on a kaiser roll with french fries and a fried pickle</div>
  <div class="box" style="left:610px;top:78px;width:270px;height:252px">
    <div class="item"><div class="row"><span>Bruschetta Chicken</span><span class="price">7.59</span></div><div class="desc">Bruschetta salsa, pesto, provolone cheese, balsamic drizzle on a French baguette, served with French fries.</div></div>
    <div class="item"><div class="row"><span>Chicken Parmigiana</span><span class="price">7.59</span></div><div class="desc">Served on a Kaiser roll with French fries.</div></div>
    <div class="item"><div class="row"><span>Chicken Portabella</span><span class="price">8.59</span></div><div class="desc">Grilled chicken, roasted red peppers, grilled portabella, lettuce, provolone and a creamy peppercorn aioli, on a French baguette, served with French fries.</div></div>
    <div class="item"><div class="row"><span>Classic BLT</span><span class="price">6.59</span></div><div class="desc">Served with potato chips.</div></div>
    <div class="item"><div class="row"><span>Crab Cake</span><span class="price">9.99</span></div><div class="desc">Lettuce, tomato and tartar sauce, served on a Kaiser roll with French fries.</div></div>
    <div class="item"><div class="row"><span>Fish Taco</span><span class="price">7.99</span></div><div class="desc">Fried wahoo in a flour tortilla with chipotle mayo, shredded lettuce, red onion and pico de gallo, finished with an avocado cream, served with potato chips.</div></div>
    <div class="item"><div class="row"><span>French Dip</span><span class="price">8.59</span></div><div class="desc">Thinly sliced Roast beef on a French baguette served with au jus, creamy horseradish sauce and French fries.</div></div>
    <div class="item"><div class="row"><span>Grilled Cheese</span><span class="price">2.99</span></div><div class="desc">Served with potato chips. Add bacon, ham or tomato.</div></div>
    <div class="item"><div class="row"><span>Grilled Chicken</span><span class="price">4.99 / 6.99</span></div><div class="desc">Lettuce, tomato, served on a Kaiser roll with French fries.</div></div>
    <div class="item"><div class="row"><span>Grilled Chicken Club</span><span class="price">8.99</span></div><div class="desc">Bacon, avocado, Swiss cheese, lettuce, tomato and roasted garlic mayonnaise on a French baguette.</div></div>
    <div class="item"><div class="row"><span>Italian Eggplant</span><span class="price">7.99</span></div><div class="desc">Grilled eggplant, roasted red peppers, red onion, melted mozzarella and garlic aioli on a French baguette.</div></div>
    <div class="item"><div class="row"><span>Roasted Turkey Cobb</span><span class="price">8.99</span></div><div class="desc">Roasted turkey breast, lettuce, tomatoes, avocado, bacon, bleu cheese dressing and Dijon mayonnaise, served on a French baguette.</div></div>
    <div class="item"><div class="row"><span>Tuna Melt</span><span class="price">6.99</span></div><div class="desc">Served with French fries.</div></div>
    <div class="item"><div class="row"><span>Turkey Club</span><span class="price">7.59</span></div><div class="desc">Served with potato chips.</div></div>
  </div>

  <h2 class="heading" style="left:610px;top:342px;width:270px">Gourmet Wraps</h2>
  <div class="tag" style="left:648px;top:364px;width:188px">Available in spinach, sundried tomato and flour tortilla, served with french fries &amp; a fried pickle</div>
  <div class="box" style="left:610px;top:388px;width:270px;height:52px">
    <div class="item"><div class="row"><span>Buffalo Chicken</span><span class="price">7.99</span></div><div class="desc">Buffalo sauce, shredded lettuce, bleu cheese dressing.</div></div>
    <div class="item"><div class="row"><span>Caprese Wrap</span><span class="price">8.99</span></div><div class="desc">Chicken, buffalo mozzarella, tomato, Romaine lettuce drizzled with a balsamic reduction.</div></div>
    <div class="item"><div class="row"><span>Chicken Caesar</span><span class="price">7.99</span></div><div class="desc">Romaine lettuce, classic Caesar salad dressing.</div></div>
  </div>

  <h2 class="heading" style="left:610px;top:446px;width:270px">Gourmet Paninis</h2>
  <div class="box" style="left:610px;top:470px;width:270px;height:70px">
    <div class="item"><div class="row"><span>Turkey Reuben</span><span class="price">8.99</span></div><div class="desc">Roasted turkey, coleslaw, Russian dressing, Swiss cheese.</div></div>
    <div class="item"><div class="row"><span>Classic Italian</span><span class="price">8.59</span></div><div class="desc">Italian sausage, fontina cheese, red bell peppers, onion.</div></div>
    <div class="item"><div class="row"><span>Chicken Pesto</span><span class="price">7.99</span></div><div class="desc">Basil pesto spread, Roma tomatoes, spinach, provolone cheese.</div></div>
    <div class="item"><div class="row"><span>Gourmet</span><span class="price">7.99</span></div><div class="desc">Grilled chicken, fresh basil, roasted red peppers, American cheese, horseradish sauce.</div></div>
  </div>

  <h2 class="heading" style="left:610px;top:553px;width:270px">Side Dishes</h2>
  <div class="box list" style="left:610px;top:576px;width:270px;height:82px">
    <div class="row"><span>French Fries</span><span class="price">3.59</span></div>
    <div class="row"><span>Cheese Fries</span><span class="price">4.59</span></div>
    <div class="row"><span>Sauteed Spinach with Garlic</span><span class="price">4.99</span></div>
    <div class="row"><span>Meatballs</span><span class="price">4.99</span></div>
    <div class="row"><span>Sausage</span><span class="price">4.99</span></div>
    <div class="row"><span>Sauteed Brocolli Rabe</span><span class="price">6.99</span></div>
    <div class="row"><span>Sauteed Vegetable DuJour</span><span class="price">4.99</span></div>
    <div class="row"><span>Linguini, Capellini, or Penne with Tomato Sauce</span><span class="price">&nbsp;</span></div>
  </div>

  <h2 class="heading" style="left:888px;top:38px;width:276px">Gourmet Salads</h2>
  <div class="tag" style="left:896px;top:58px;width:236px">French, Russian, Creamy Italian, Bleu Cheese, Honey Mustard, Balsamic Vinaigrette, Fat-Free Italian and Ranch Dressing</div>
  <div class="box" style="left:888px;top:86px;width:274px;height:214px">
    <div class="item"><div class="row"><span>Tossed</span><span class="price">7.59</span></div><div class="desc">With Grilled Chicken</div></div>
    <div class="item"><div class="row"><span>Caesar Salad</span><span class="price">8.99 / 7.99</span></div><div class="desc">With Chicken</div></div>
    <div class="item"><div class="row"><span>Barbecue Chicken</span><span class="price">9.59</span></div><div class="desc">Tomatoes, corn, onions, black beans, cilantro, mozzarella cheese, crunchy sweet onion strips, served with barbecue-ranch dressing.</div></div>
    <div class="item"><div class="row"><span>Bruschetta</span><span class="price">8.99</span></div><div class="desc">Chicken, diced tomatoes, Kalamata olives, provolone cheese, parmesan toasted crostini, served with a balsamic vinaigrette dressing.</div></div>
    <div class="item"><div class="row"><span>Buffalo Chicken</span><span class="price">8.99</span></div><div class="desc">Chicken, Gorgonzola cheese, celery, red onion, black olives, cucumber, served with bleu cheese dressing.</div></div>
    <div class="item"><div class="row"><span>Cranberry Spinach</span><span class="price">8.99</span></div><div class="desc">Spinach, dried cranberries, mandarin oranges, roasted almonds, feta cheese, served with balsamic vinaigrette.</div></div>
    <div class="item"><div class="row"><span>Gourmet Cobb</span><span class="price">9.59</span></div><div class="desc">Roasted turkey, bacon, feta cheese, tomatoes, croutons, avocado, served with a creamy garlic dressing.</div></div>
    <div class="item"><div class="row"><span>Gourmet Wedge</span><span class="price">8.99</span></div><div class="desc">Two individual lettuce wedges topped with Gorgonzola, bacon, Roma tomatoes, served with a creamy parmesan dressing.</div></div>
    <div class="item"><div class="row"><span>Honey Crisp</span><span class="price">8.99</span></div><div class="desc">Breaded chicken tenders, cucumbers, hard boiled eggs, corn, tomatoes, served with honey mustard dressing.</div></div>
    <div class="item"><div class="row"><span>Santa Fe</span><span class="price">9.59</span></div><div class="desc">Blackened chicken, red onions, roasted red peppers, pepperjack and cheddar cheeses, sliced avocados, corn, diced tomatoes, crisp tortilla strips, tossed with Santa Fe dressing.</div></div>
    <div class="item"><div class="row"><span>Tomato and Mozzarella Capri</span><span class="price">9.99</span></div><div class="desc">Sliced tomatoes, fresh mozzarella, basil, served with a balsamic glaze, field greens.</div></div>
  </div>

  <h2 class="heading" style="left:888px;top:314px;width:276px">Lunch Abilities</h2>
  <div class="tag" style="left:948px;top:334px;width:158px">A smaller portion of some of your gourmet favorites</div>
  <div class="box list" style="left:888px;top:350px;width:274px;height:86px">
    <div class="row"><span>Baked Penne Pasta</span><span class="price">7.99</span></div>
    <div class="row"><span>Chicken Parmigiana</span><span class="price">8.99</span></div>
    <div class="row"><span>Chicken Rosa</span><span class="price">8.99</span></div>
    <div class="row"><span>Eggplant Parmigiana</span><span class="price">8.99</span></div>
    <div class="row"><span>Chicken Francaise</span><span class="price">8.99</span></div>
    <div class="row"><span>Penne Italiano</span><span class="price">8.99</span></div>
    <div class="row"><span>Linguini and Clams</span><span class="price">8.99</span></div>
    <div class="row"><span>Add a House Salad or Cup of Soup Du Jour</span><span class="price">2.99</span></div>
  </div>

  <h2 class="heading" style="left:888px;top:441px;width:276px">Homemade Soups</h2>
  <div class="box list" style="left:888px;top:462px;width:274px;height:34px">
    <div class="row"><span>Soup Du Jour Cream of Broccoli</span><span class="price">3.99</span></div>
    <div class="row"><span>French Onion</span><span class="price">4.59</span></div>
    <div class="row"><span>Italian Minestrone</span><span class="price">3.59</span></div>
  </div>

  <h2 class="heading" style="left:888px;top:505px;width:276px">Great Beginings</h2>
  <div class="box" style="left:888px;top:534px;width:274px;height:126px">
    <div class="item"><div class="row"><span>Tuscan Mushrooms</span><span class="price">8.99</span></div><div class="desc">Stuffed with roasted red peppers, green olives, scallions, panko breadcrumbs, Pecorino Romano and mozzarella cheese.</div></div>
    <div class="item"><div class="row"><span>Crabcakes</span><span class="price">11.99</span></div><div class="desc">Drizzled with a spicy mustard sauce.</div></div>
    <div class="item"><div class="row"><span>Gourmet Mac and Cheese Balls</span><span class="price">7.99</span></div><div class="desc">Pasta and three cheeses wrapped in Italian bread crumbs over a bed of Rosa sauce.</div></div>
    <div class="item"><div class="row"><span>Roasted Garlic Hummus</span><span class="price">6.99</span></div><div class="desc">Served with toasted pita bread.</div></div>
    <div class="item"><div class="row"><span>Pot Stickers</span><span class="price">9.59</span></div><div class="desc">Stuffed with ground pork and vegetables, served with a spicy dipping sauce, sweet chili paste.</div></div>
    <div class="item"><div class="row"><span>Artichoke and Spinach Dip</span><span class="price">8.99</span></div><div class="desc">Served with parmesan crostini.</div></div>
    <div class="item"><div class="row"><span>Asian Lettuce Wraps</span><span class="price">8.99</span></div><div class="desc">Chicken and vegetables in a sweet hoisin sauce, served in crisp lettuce cups.</div></div>
  </div>

  <div class="photo-strip ph-steak" role="img" aria-label="Photo of grilled steak with asparagus"></div>
  <div class="photo-strip ph-pasta" role="img" aria-label="Photo of seafood spaghetti in red sauce"></div>
  <div class="photo-strip ph-gnocchi" role="img" aria-label="Photo of creamy pasta with broccoli"></div>

</div>
</body>
</html>
```